Harbor Bloom_The Copper Lantern

I am looking for someone to take three articles and package them with a front and back cover. The first two stories are completed and included. The third story will be completed by the end of the contest. I need a format, or template to easily edit all three stories.

Target Market(s)

Business professionals

Requirements
Must have
• HARBOR Bloom logo and tenets on the front. An easy method to edit stories in the series. Easy template to use, maybe utilizing Word, Lucid Press, or PowerPoint to hold articles.
Nice to have
• On a platform that can be contented to social media for sharing and comment such as Simplebooklet

```html
<!DOCTYPE html>
<html lang="en">
<head>
<meta charset="utf-8">
<title>Harbor Bloom — The Copper Lantern</title>
<link href="https://fonts.googleapis.com/css2?family=Archivo:wght@700;800;900&family=Open+Sans:wght@400;600;700&display=swap" rel="stylesheet">
<style>
  :root {
    --bg: #e6e6e6;
    --paper: #ffffff;
    --brand-blue: #5f8fc6;
    --title-blue: #3a69a3;
    --navy: #2c4f7c;
    --ink: #3a3a3a;
    --muted: #8a8a8a;
    --rule: #d0d0d0;
    --panel: #efefef;
  }
  * { margin: 0; padding: 0; box-sizing: border-box; }
  html, body { width: 1200px; height: 2688px; overflow: hidden; background: var(--bg); }
  body { position: relative; font-family: "Open Sans", Arial, sans-serif; color: var(--ink); }

  .sheet { position: absolute; left: 0; width: 1200px; height: 896px; }
  .sheet--cover { top: 0; }
  .sheet--spread { top: 896px; }
  .sheet--back { top: 1792px; }

  .page {
    position: absolute; background: var(--paper);
    box-shadow: 0 14px 30px rgba(0,0,0,.14), 0 2px 6px rgba(0,0,0,.08);
    overflow: hidden;
  }
  .sheet--cover .page, .sheet--back .page { left: 280px; top: 33px; width: 640px; height: 830px; }
  .sheet--spread .page { top: 98px; width: 540px; height: 700px; }
  .page--left { left: 60px; }
  .page--right { left: 600px; }
  .spine { position: absolute; left: 598px; top: 98px; width: 4px; height: 700px; background: linear-gradient(90deg, rgba(0,0,0,.12), rgba(0,0,0,0)); z-index: 2; }

  .masthead { position: absolute; top: 0; left: 0; right: 0; height: 118px; display: flex; }
  .masthead__logo { width: 178px; display: flex; align-items: center; justify-content: center; gap: 8px; }
  .brand-mark { width: 12px; height: 12px; background: var(--brand-blue); }
  .brand-name { font-family: "Archivo", Arial, sans-serif; font-weight: 800; font-size: 15px; color: var(--brand-blue); letter-spacing: .5px; }
  .masthead__band { flex: 1; background: var(--brand-blue); color: #fff; padding: 18px 26px; font-family: "Archivo", Arial, sans-serif; font-weight: 900; font-size: 40px; line-height: 1; letter-spacing: 1px; }

  .cover-title { position: absolute; top: 134px; left: 178px; right: 26px; font-family: "Archivo", Arial, sans-serif; font-weight: 800; font-size: 34px; line-height: 1.08; color: var(--title-blue); }
  .cover-rule { position: absolute; left: 178px; right: 26px; top: 222px; height: 2px; background: var(--title-blue); }

  .col { position: absolute; }
  .copy { font-size: 8.5px; line-height: 13px; color: var(--ink); margin-bottom: 8px; text-align: justify; }
  .small-head { font-family: "Archivo", Arial, sans-serif; font-weight: 800; font-size: 11px; color: var(--title-blue); text-transform: uppercase; letter-spacing: .6px; margin-bottom: 8px; }

  .visual { border-radius: 4px; }
  .visual--wheel { width: 200px; height: 200px; border-radius: 50%; margin: 2px auto 12px; background: conic-gradient(#f2a7c1, #c9a3e0, #9fb6ec, #8fd5d0, #b5e0a0, #f2dd8e, #f5b98a, #f2a7c1); }
  .visual--target { width: 150px; height: 150px; border-radius: 50%; background: radial-gradient(circle, #f6d45c 0 22%, #e67d3c 23% 45%, #5fae5a 46% 68%, #5b86c9 69% 100%); }
  .visual--photo { width: 100%; height: 170px; background: linear-gradient(135deg, #9aa7b5, #c8c2b4 55%, #6e7b8a); margin-bottom: 10px; }
  .visual--diagram { width: 100%; height: 80px; background: linear-gradient(180deg, #f4f6f9, #dfe6ef); border: 1px solid var(--rule); margin-bottom: 10px; }

  .tenet-band { position: absolute; top: 332px; left: 0; right: 0; height: 58px; background: var(--navy); color: #fff; display: flex; align-items: center; font-family: "Archivo", Arial, sans-serif; font-weight: 700; font-size: 15px; }
  .page--left .tenet-band { padding-left: 36px; }

  .page-head { position: absolute; top: 0; left: 0; right: 0; height: 6px; background: var(--brand-blue); }

  .back-box { position: absolute; left: 36px; top: 60px; width: 250px; height: 124px; background: var(--panel); border: 1px solid var(--rule); }
  .back-brand { position: absolute; left: 36px; bottom: 40px; display: flex; align-items: center; gap: 12px; }
  .back-brand .brand-mark { width: 30px; height: 30px; }
  .back-brand .brand-name { font-size: 36px; color: var(--title-blue); }
  .back-rule { position: absolute; left: 36px; width: 250px; bottom: 100px; height: 1px; background: var(--rule); }
</style>
</head>
<body>

<!-- Front cover -->
<section class="sheet sheet--cover">
  <article class="page">
    <header class="masthead">
      <div class="masthead__logo"><span class="brand-mark"></span><span class="brand-name">HARBOR BLOOM</span></div>
      <div class="masthead__band">HARBOR<br>BLOOM</div>
    </header>
    <h1 class="cover-title">Failure in Diversity is<br>The Copper Lantern</h1>
    <div class="cover-rule"></div>

    <div class="col" style="left:26px; top:140px; width:136px;">
      <p class="copy">Teams that welcome different voices make stronger choices. Leaders must listen, invite dissent and act with courage when the stakes are high.</p>
      <p class="copy">Real inclusion is built daily through small decisions, honest feedback and steady support for every member of the group.</p>
      <p class="copy">When managers avoid hard conversations, talent quietly leaves and trust erodes. Naming the problem early is the first sign of real nerve.</p>
      <p class="copy">Measure progress with clear goals, review hiring and promotion data each quarter, and share results openly with the whole organisation.</p>
      <p class="copy">Mentoring programs pair new staff with experienced guides, building networks that help people grow, stay and lead with confidence.</p>
      <p class="copy">Diverse boards ask better questions. They test assumptions, widen the view of risk and spot opportunities others miss entirely.</p>
      <p class="copy">Teams that welcome different voices make stronger choices. Leaders must listen, invite dissent and act with courage when the stakes are high.</p>
    </div>

    <div class="col" style="left:178px; top:240px; width:210px;">
      <p class="copy">Teams that welcome different voices make stronger choices. Leaders must listen, invite dissent and act with courage when the stakes are high.</p>
      <p class="copy">Real inclusion is built daily through small decisions, honest feedback and steady support for every member of the group.</p>
      <p class="copy">When managers avoid hard conversations, talent quietly leaves and trust erodes. Naming the problem early is the first sign of real nerve.</p>
      <p class="copy">Measure progress with clear goals, review hiring and promotion data each quarter, and share results openly with the whole organisation.</p>
      <p class="copy">Mentoring programs pair new staff with experienced guides, building networks that help people grow, stay and lead with confidence.</p>
      <p class="copy">Diverse boards ask better questions. They test assumptions, widen the view of risk and spot opportunities others miss entirely.</p>
      <p class="copy">Teams that welcome different voices make stronger choices. Leaders must listen, invite dissent and act with courage when the stakes are high.</p>
      <p class="copy">Real inclusion is built daily through small decisions, honest feedback and steady support for every member of the group.</p>
    </div>

    <div class="col" style="left:404px; top:240px; width:210px;">
      <h2 class="small-head">Circles of Identity</h2>
      <div class="visual visual--wheel" role="img" aria-label="Colourful identity wheel diagram"></div>
      <p class="copy">When managers avoid hard conversations, talent quietly leaves and trust erodes. Naming the problem early is the first sign of real nerve.</p>
      <p class="copy">Measure progress with clear goals, review hiring and promotion data each quarter, and share results openly with the whole organisation.</p>
      <p class="copy">Mentoring programs pair new staff with experienced guides, building networks that help people grow, stay and lead with confidence.</p>
      <p class="copy">Diverse boards ask better questions. They test assumptions, widen the view of risk and spot opportunities others miss entirely.</p>
    </div>
  </article>
</section>

<!-- Inside spread -->
<section class="sheet sheet--spread">
  <article class="page page--left">
    <div class="page-head"></div>
    <div class="col" style="left:36px; top:30px; width:468px;">
      <h2 class="small-head">Our Tenets</h2>
    </div>
    <div class="col" style="left:36px; top:60px; width:160px;">
      <div class="visual visual--target" role="img" aria-label="Layered circle diagram of influence"></div>
    </div>
    <div class="col" style="left:210px; top:54px; width:160px;">
      <div class="visual visual--wheel" style="width:160px;height:160px;margin:0;" role="img" aria-label="Colourful identity wheel diagram"></div>
    </div>
    <div class="col" style="left:386px; top:60px; width:118px;">
      <p class="copy">Each ring shows a layer of identity, from core traits to the roles we hold at work and in our communities.</p>
      <p class="copy">Use the wheel to map the strengths your team already has and the voices still missing.</p>
    </div>
    <div class="col" style="left:36px; top:236px; width:222px;">
      <p class="copy">Teams that welcome different voices make stronger choices. Leaders must listen, invite dissent and act with courage when the stakes are high.</p>
    </div>
    <div class="col" style="left:282px; top:236px; width:222px;">
      <p class="copy">Real inclusion is built daily through small decisions, honest feedback and steady support for every member of the group.</p>
    </div>
    <div class="tenet-band">Courage turns good intentions into lasting change.</div>
    <div class="col" style="left:36px; top:412px; width:222px;">
      <p class="copy">Teams that welcome different voices make stronger choices. Leaders must listen, invite dissent and act with courage when the stakes are high.</p>
      <p class="copy">Real inclusion is built daily through small decisions, honest feedback and steady support for every member of the group.</p>
      <p class="copy">When managers avoid hard conversations, talent quietly leaves and trust erodes. Naming the problem early is the first sign of real nerve.</p>
      <p class="copy">Measure progress with clear goals, review hiring and promotion data each quarter, and share results openly with the whole organisation.</p>
      <p class="copy">Mentoring programs pair new staff with experienced guides, building networks that help people grow, stay and lead with confidence.</p>
    </div>
    <div class="col" style="left:282px; top:412px; width:222px;">
      <p class="copy">Diverse boards ask better questions. They test assumptions, widen the view of risk and spot opportunities others miss entirely.</p>
      <p class="copy">Teams that welcome different voices make stronger choices. Leaders must listen, invite dissent and act with courage when the stakes are high.</p>
      <p class="copy">Real inclusion is built daily through small decisions, honest feedback and steady support for every member of the group.</p>
      <p class="copy">When managers avoid hard conversations, talent quietly leaves and trust erodes. Naming the problem early is the first sign of real nerve.</p>
      <p class="copy">Measure progress with clear goals, review hiring and promotion data each quarter, and share results openly with the whole organisation.</p>
    </div>
  </article>

  <article class="page page--right">
    <div class="page-head"></div>
    <div class="col" style="left:36px; top:30px; width:468px;">
      <h2 class="small-head">Key Findings</h2>
      <div class="visual visual--diagram" role="img" aria-label="Small flow diagram of findings"></div>
    </div>
    <div class="col" style="left:36px; top:148px; width:222px;">
      <p class="copy">Teams that welcome different voices make stronger choices. Leaders must listen, invite dissent and act with courage when the stakes are high.</p>
      <p class="copy">Real inclusion is built daily through small decisions, honest feedback and steady support for every member of the group.</p>
      <p class="copy">When managers avoid hard conversations, talent quietly leaves and trust erodes. Naming the problem early is the first sign of real nerve.</p>
    </div>
    <div class="col" style="left:282px; top:148px; width:222px;">
      <p class="copy">Measure progress with clear goals, review hiring and promotion data each quarter, and share results openly with the whole organisation.</p>
      <p class="copy">Mentoring programs pair new staff with experienced guides, building networks that help people grow, stay and lead with confidence.</p>
      <p class="copy">Diverse boards ask better questions. They test assumptions, widen the view of risk and spot opportunities others miss entirely.</p>
    </div>
    <div class="tenet-band"></div>
    <div class="col" style="left:36px; top:412px; width:222px;">
      <p class="copy">Teams that welcome different voices make stronger choices. Leaders must listen, invite dissent and act with courage when the stakes are high.</p>
      <p class="copy">Real inclusion is built daily through small decisions, honest feedback and steady support for every member of the group.</p>
      <p class="copy">When managers avoid hard conversations, talent quietly leaves and trust erodes. Naming the problem early is the first sign of real nerve.</p>
      <p class="copy">Measure progress with clear goals, review hiring and promotion data each quarter, and share results openly with the whole organisation.</p>
      <p class="copy">Mentoring programs pair new staff with experienced guides, building networks that help people grow, stay and lead with confidence.</p>
    </div>
    <div class="col" style="left:282px; top:412px; width:222px;">
      <div class="visual visual--photo" role="img" aria-label="Photo of colleagues meeting in an office"></div>
      <p class="copy">Diverse boards ask better questions. They test assumptions, widen the view of risk and spot opportunities others miss entirely.</p>
      <p class="copy">Real inclusion is built daily through small decisions, honest feedback and steady support for every member of the group.</p>
    </div>
  </article>
  <div class="spine"></div>
</section>

<!-- Back cover -->
<section class="sheet sheet--back">
  <article class="page">
    <div class="col" style="left:36px; top:40px; width:568px;">
      <h2 class="small-head">Upcoming Stories</h2>
    </div>
    <div class="back-box"></div>
    <div class="col" style="left:302px; top:60px; width:302px;">
      <p class="copy">Teams that welcome different voices make stronger choices. Leaders must listen, invite dissent and act with courage when the stakes are high.</p>
      <p class="copy">Real inclusion is built daily through small decisions, honest feedback and steady support for every member of the group.</p>
      <p class="copy">Mentoring programs pair new staff with experienced guides, building networks that help people grow, stay and lead with confidence.</p>
    </div>
    <div class="col" style="left:36px; top:204px; width:274px;">
      <p class="copy">When managers avoid hard conversations, talent quietly leaves and trust erodes. Naming the problem early is the first sign of real nerve.</p>
      <p class="copy">Measure progress with clear goals, review hiring and promotion data each quarter, and share results openly with the whole organisation.</p>
      <p class="copy">Mentoring programs pair new staff with experienced guides, building networks that help people grow, stay and lead with confidence.</p>
      <p class="copy">Diverse boards ask better questions. They test assumptions, widen the view of risk and spot opportunities others miss entirely.</p>
      <p class="copy">Teams that welcome different voices make stronger choices. Leaders must listen, invite dissent and act with courage when the stakes are high.</p>
      <p class="copy">Real inclusion is built daily through small decisions, honest feedback and steady support for every member of the group.</p>
      <p class="copy">When managers avoid hard conversations, talent quietly leaves and trust erodes. Naming the problem early is the first sign of real nerve.</p>
      <p class="copy">Measure progress with clear goals, review hiring and promotion data each quarter, and share results openly with the whole organisation.</p>
      <p class="copy">Diverse boards ask better questions. They test assumptions, widen the view of risk and spot opportunities others miss entirely.</p>
    </div>
    <div class="col" style="left:330px; top:204px; width:274px;">
      <p class="copy">Real inclusion is built daily through small decisions, honest feedback and steady support for every member of the group.</p>
      <p class="copy">Teams that welcome different voices make stronger choices. Leaders must listen, invite dissent and act with courage when the stakes are high.</p>
      <p class="copy">Diverse boards ask better questions. They test assumptions, widen the view of risk and spot opportunities others miss entirely.</p>
      <p class="copy">When managers avoid hard conversations, talent quietly leaves and trust erodes. Naming the problem early is the first sign of real nerve.</p>
      <p class="copy">Mentoring programs pair new staff with experienced guides, building networks that help people grow, stay and lead with confidence.</p>
      <p class="copy">Measure progress with clear goals, review hiring and promotion data each quarter, and share results openly with the whole organisation.</p>
      <p class="copy">Teams that welcome different voices make stronger choices. Leaders must listen, invite dissent and act with courage when the stakes are high.</p>
      <p class="copy">Real inclusion is built daily through small decisions, honest feedback and steady support for every member of the group.</p>
    </div>
    <div class="back-rule"></div>
    <div class="back-brand"><span class="brand-mark"></span><span class="brand-name">HARBOR BLOOM</span></div>
  </article>
</section>

</body>
</html>
```